BrightWave Tristate Commercial Cleaning Brochure

We need a tri fold brochure that we can use to market our commercial cleaning services to clients. We are looking for something that will stand out. We don't want to use any faces of people on the brochures, only cleaning tools and supplies. We offer Office Cleaning, Covid Cleaning, Janitorial and Floor Services

Target Market(s)

Small to large businesses

Industry/Entity Type

Commercial Cleaning

Colors
0054AA
0677BA
7BADD7
CADEEF
E8F1F8
0094D4
00A9DD
6FCCEA
C7EBF8
E9F6FB
00AB8E
00BBA5
67D7C9
C6EFE9
E9F9F6
59FF00
82FF00
B8FF75
E3FFCB
F4FFEA

Requirements
Must have
• Stand out design-Eye Catching
Should not have
• faces of ppl the brochure

```html
<!DOCTYPE html>
<html lang="en">
<head>
<meta charset="utf-8">
<title>BrightWave Tristate – Commercial Cleaning Brochure</title>
<link href="https://fonts.googleapis.com/css2?family=Roboto:wght@400;500;700;900&display=swap" rel="stylesheet">
<style>
:root{
  --blue:#0054AA;
  --blue-deep:#0b4f9c;
  --green:#8CC63F;
  --green-text:#7DB52E;
  --white:#ffffff;
  --ink-blue:#0a4a94;
  --page:#eef1f4;
  --sky:#cfe6f6;
  --grey-soft:#e6e8ea;
}
*{margin:0;padding:0;box-sizing:border-box}
html,body{width:1200px;height:3500px;overflow:hidden}
body{background:var(--page);font-family:"Roboto",Arial,sans-serif;position:relative}
.spread{position:absolute;left:60px;width:1080px;height:838px;background:var(--white);overflow:hidden;box-shadow:0 18px 40px rgba(0,0,0,.18)}
.spread--outside{top:160px}
.spread--inside{top:1160px}
.panel{position:absolute;top:0;width:360px;height:838px}
.abs{position:absolute}
.wave{position:absolute;left:0;top:0}

/* outside */
.covid-sky{left:0;top:0;width:360px;height:150px;background:linear-gradient(180deg,#eaf4fb,#cfe6f6 70%,#fff)}
.covid-title{left:30px;top:40px;font-size:33px;font-weight:500;color:var(--blue)}
.covid-sub{left:30px;top:168px;width:300px;font-size:19px;line-height:23px;color:var(--green-text);font-weight:500}
.covid-intro{left:32px;top:270px;width:300px;font-size:14.5px;line-height:18px;color:var(--blue)}
.covid-photo{left:0;top:330px;width:360px;height:330px;background:linear-gradient(160deg,#f4f6f8,#c9cfd6 60%,#8a939c)}
.covid-foot{left:30px;top:712px;width:305px;font-size:14px;line-height:18px;color:var(--white)}

.contact{left:360px;background:var(--green)}
.contact-title{left:0;top:42px;width:360px;text-align:center;font-size:34px;font-weight:500;color:var(--white)}
.contact-care{left:0;top:198px;width:360px;text-align:center;font-size:36px;line-height:41px;color:var(--white)}
.contact-shows{left:0;top:318px;width:360px;text-align:center;font-size:37px;line-height:42px;color:var(--white)}
.contact-any{left:0;top:532px;width:360px;text-align:center;font-size:15.5px;line-height:20px;font-weight:700;color:#1e2a10}
.call-note{left:0;top:680px;width:360px;text-align:center;font-size:14px;line-height:19px;font-weight:700;color:var(--white)}
.phone{font-size:45px;font-weight:700;color:var(--white);letter-spacing:1px;text-align:center;width:360px;left:0}
.phone--contact{top:762px}

.cover{left:720px}
.brand{left:0;top:92px;width:360px;text-align:center;font-size:38px;font-weight:500;color:var(--blue)}
.brand-mark{display:inline-block;width:16px;height:16px;border-radius:50%;background:var(--green);margin-right:10px;vertical-align:middle}
.cover-head{left:0;top:238px;width:360px;text-align:center;line-height:1}
.cover-head span{display:block}
.h-commercial{font-size:30px;font-weight:500;color:var(--blue)}
.h-cleaning{font-size:40px;font-weight:500;color:var(--green);margin-top:4px}
.h-services{font-size:42px;font-weight:900;color:var(--blue);margin-top:2px}
.supplies{left:0;top:355px;width:360px;height:262px;background:radial-gradient(ellipse at 50% 60%,#f3d34a 0%,#8cc63f 30%,#e57a8a 55%,#f4f4f4 80%)}
.offer-title{left:0;top:680px;width:360px;text-align:center;font-size:32px;color:var(--white)}
.offer-list{left:0;top:722px;width:360px;text-align:center;font-size:19.5px;line-height:25px;color:var(--white)}
.phone--cover{top:768px}

/* inside */
.inside-body{background:linear-gradient(90deg,#ffffff 40%,#e3e5e7)}
.head-text{left:40px;top:34px;color:var(--white)}
.head-text .pro{display:block;font-size:24px}
.head-text .topic{display:block;font-size:34px;font-weight:500;margin-top:2px}
.head-text .svc{display:block;font-size:24px;margin-top:2px}
.body-copy{left:38px;width:288px;font-size:15.5px;line-height:19.5px;color:var(--ink-blue);text-align:justify}
.body-copy p+p{margin-top:19px}
.office-photo{left:0;top:560px;width:720px;height:278px;background:linear-gradient(180deg,#f1f2f3,#b7b3ad 45%,#5d544c)}
.floor-round{border-radius:50%}
.floor-round--vacuum{left:38px;top:165px;width:155px;height:155px;background:radial-gradient(circle,#9aa0a6,#4b5157)}
.floor-round--mop{left:185px;top:135px;width:215px;height:215px;background:radial-gradient(circle at 50% 40%,#f7f8f9,#c8ccd0 60%,#9fc94d 61%,#dfe2e4 70%)}
</style>
</head>
<body>

<!-- Outside spread -->
<section class="spread spread--outside">
  <div class="panel">
    <div class="abs covid-sky" role="img" aria-label="Light blue background with floating virus particles"></div>
    <svg class="wave" width="360" height="180" viewBox="0 0 360 180"><path d="M0 120 C90 95 200 95 300 118" stroke="var(--blue)" stroke-width="7" fill="none"/></svg>
    <div class="abs covid-title">Covid Cleaning</div>
    <div class="abs covid-sub">COVID-19 CLEANING &amp; DISINFECTING SERVICES Protect Your Employees &amp; Guests From COVID-19</div>
    <div class="abs covid-intro">We provide customized COVID-19 cleaning and disinfection services for businesses that want to prevent an outbreak in their facility.</div>
    <div class="abs covid-photo" role="img" aria-label="Worker in protective suit spraying disinfectant in an office"></div>
  </div>
  <div class="panel contact">
    <div class="abs contact-title">Contact Us</div>
    <svg class="wave" width="360" height="160" viewBox="0 0 360 160"><path d="M40 125 C110 150 170 110 230 108 C270 106 300 115 320 125" stroke="var(--white)" stroke-width="6" fill="none" stroke-linecap="round"/></svg>
    <div class="abs contact-care">WE CARE ABOUT<br>CLEAN</div>
    <div class="abs contact-shows">And It Shows In<br>Our Work, Our<br>People, Our<br>Accountability</div>
    <div class="abs contact-any">ANY INDUSTRY. ANY BUILDING.<br>ANY ENVIRONMENT.<br>WE CLEAN IT ALL.</div>
  </div>
  <div class="panel cover">
    <div class="abs brand"><span class="brand-mark"></span>BrightWave Tristate</div>
    <div class="abs cover-head">
      <span class="h-commercial">COMMERCIAL</span>
      <span class="h-cleaning">CLEANING</span>
      <span class="h-services">SERVICES</span>
    </div>
    <div class="abs supplies" role="img" aria-label="Cleaning supplies: spray bottle, bucket, sponges, cloth, brush and rubber gloves"></div>
  </div>
  <svg class="wave" width="1080" height="838" viewBox="0 0 1080 838"><path d="M0 636 C200 660 300 690 420 680 C560 668 620 590 760 598 C900 606 1000 640 1080 664 L1080 838 L0 838 Z" fill="var(--blue)"/></svg>
  <div class="abs covid-foot">With our national disinfection expertise, over many years of experience, and specialized skills in providing cleaning services to health-care facilities, we are prepared to handle the unique needs that this pandemic has created.</div>
  <div class="abs call-note" style="left:360px">FIND YOUR CLOSEST<br>SPARKLECORE LOCATION<br>TO CUSTOMIZE YOUR CLEAN<br>CALL US NOW</div>
  <div class="abs phone phone--contact" style="left:360px">1234567890</div>
  <div class="abs offer-title" style="left:720px">We offer</div>
  <div class="abs offer-list" style="left:720px">Office Cleaning, Covid Cleaning,<br>Janitorial &amp; Floor Services</div>
  <div class="abs phone phone--cover" style="left:720px">1234567890</div>
</section>

<!-- Inside spread -->
<section class="spread spread--inside">
  <div class="panel inside-body" style="left:0"></div>
  <div class="panel inside-body" style="left:360px"></div>
  <div class="abs office-photo" role="img" aria-label="Empty open-plan office with desks, chairs and monitors"></div>
  <svg class="wave" width="1080" height="300" viewBox="0 0 1080 300">
    <path d="M0 0 H360 V145 C250 140 120 160 0 200 Z" fill="var(--blue)"/>
    <path d="M360 0 H720 V150 C600 140 470 145 360 148 Z" fill="var(--blue-deep)"/>
    <path d="M720 0 H1080 V130 C980 150 860 170 720 172 Z" fill="var(--blue)"/>
  </svg>
  <div class="abs head-text"><span class="pro">Professional</span><span class="topic">Office Cleaning</span><span class="svc">Services</span></div>
  <div class="abs head-text" style="left:400px;top:32px"><span class="pro">Professional</span><span class="topic">Janitorial Cleaning</span><span class="svc">Services</span></div>
  <div class="abs head-text" style="left:748px"><span class="pro">Professional</span><span class="topic">Floor Cleaning</span><span class="svc">Services</span></div>

  <div class="abs body-copy" style="top:255px">
    <p>We make use of eco-friendly products and advanced equipment during the cleaning process. Moreover, we have a team of highly expert cleaning professionals who have years of experience under their belt, and they are highly trained and skilled as well.</p>
    <p>You are assured to have complete peace of mind as we hire them only after police verification as well as medical checkups. When you would hire for the office cleaning services, then you would be assured of getting the best quality attention in a rather professional way.</p>
  </div>
  <div class="abs body-copy" style="left:396px;top:255px">
    <p>Janitorial services relate to commercial property cleaning, including professional offices, educational, medical and industrial business cleaning. Some commercial janitorial services can include maintenance or property management services. Those who perform the work are referred to as custodians, janitors or cleaners.</p>
    <p>When it’s time to hire commercial cleaners, it is important to know about the different types of professional cleaning services available.</p>
  </div>

  <div class="abs floor-round floor-round--mop" style="left:905px" role="img" aria-label="Green mop on a shiny tiled floor"></div>
  <div class="abs floor-round floor-round--vacuum" style="left:758px" role="img" aria-label="Carpet being cleaned with an extraction machine"></div>
  <div class="abs body-copy" style="left:758px;top:440px;width:290px;font-size:15.5px">
    <p>Sparkling floor reflects the owner’s way of living. Floors and tiles lose their shine after a few days of cleaning. Upon vigorous scrubbing for days, they begin to wither away, and their colour fades.</p>
    <p>Polishing adds a protective layer to the object and maintains its brand new look for days together. The unique solutions and precision make polishing a difficult task, that calls for professionals.</p>
    <p>Our services include regular floor scrubbing, marble polishing, the wax coating of Vinyl flooring and wooden floor polishing.</p>
  </div>
</section>

</body>
</html>
```